Butcher shop

We have 2 butcher shops:

Shop 9, Ridgeway Court, Ashcombe NSW 2391
Ph 02 6512 3840

47 Marlow St, Kellbrook NSW 2394
Ph 02 6518 2274

ABN 48 907 215 816

I would like this info on reverse of card and my personal info on front of card. I have a logo I would like to use also. Require a very smooth thick matte card, with colour both sides.

Front of card should say:

Linda Farrugia
Accounts

Ph 0437 620 915
E lindafarrugia@quollmail.com.au

Industry/Entity Type

Shop

Contact Information for Business Card

Linda Farrugia
Ph 0437 620 915

Logo Text

Farrugia's Quality Meats

Logo styles of interest
Pictorial/Combination Logo
Requirements
Must have
• We use Century Gothic Font

```html
<!DOCTYPE html>
<html lang="en">
<head>
<meta charset="utf-8">
<title>Farrugia's Quality Meats – Business Card</title>
<link rel="stylesheet" href="https://fonts.googleapis.com/css2?family=Didact+Gothic&display=swap">
<style>
  :root {
    --sky: #8fd6f2;
    --navy: #16123f;
    --ink: #0a0a0a;
    --paper-text: #1b1850;
    --white: #ffffff;
    --stage: #2a2a2a;
  }
  * { box-sizing: border-box; margin: 0; padding: 0; }
  html, body {
    width: 1200px; height: 1200px; overflow: hidden;
    background: var(--stage);
    font-family: "Didact Gothic", "Century Gothic", sans-serif;
  }
  .canvas {
    position: relative; width: 1200px; height: 1200px;
    display: flex; flex-direction: column; align-items: center; justify-content: center; gap: 40px;
  }
  .card {
    position: relative; width: 880px; height: 538px; overflow: hidden;
    box-shadow: 0 12px 30px rgba(0,0,0,.45);
  }

  /* Front */
  .card--front { background: var(--sky); }
  .front__logo {
    position: absolute; left: 400px; top: 150px; width: 380px;
    text-align: center; color: var(--ink); font-size: 40px; line-height: 1.05;
  }
  .front__name {
    position: absolute; left: 0; top: 360px; display: flex; align-items: flex-end; gap: 6px;
    color: var(--paper-text); font-size: 46px; letter-spacing: 1px; line-height: 1;
  }
  .front__marker { width: 38px; height: 30px; background: var(--paper-text); margin-bottom: 2px; }
  .front__contact-band {
    position: absolute; left: 0; right: 0; top: 412px; height: 72px; background: var(--ink);
    display: flex; align-items: center; justify-content: space-between; padding: 0 40px 0 96px;
    color: var(--white); font-size: 24px; letter-spacing: 1px;
  }
  .front__base-band { position: absolute; left: 0; right: 0; top: 484px; bottom: 0; background: var(--navy); }

  /* Back */
  .card--back { background: var(--navy); }
  .back__shapes { position: absolute; inset: 0; }
  .back__logo {
    position: absolute; left: 20px; top: 190px; width: 400px;
    text-align: center; color: var(--ink); font-size: 52px; line-height: 1.05;
  }
  .back__details {
    position: absolute; left: 520px; top: 40px; color: var(--white);
    font-size: 24px; line-height: 1.25; letter-spacing: .5px;
  }
  .shop { margin-bottom: 38px; }
  .label, .abn { color: var(--sky); }
</style>
</head>
<body>
<main class="canvas">

  <section class="card card--front" aria-label="Card front">
    <div class="front__logo">Farrugia's<br>Quality Meats</div>
    <div class="front__name"><span class="front__marker"></span>Linda Farrugia</div>
    <div class="front__contact-band">
      <span>Ph 0437 620 915</span>
      <span>E lindafarrugia@quollmail.com.au</span>
    </div>
    <div class="front__base-band"></div>
  </section>

  <section class="card card--back" aria-label="Card back">
    <svg class="back__shapes" viewBox="0 0 880 538" width="880" height="538" aria-hidden="true">
      <circle cx="200" cy="170" r="262" fill="#000" opacity=".55"/>
      <circle cx="200" cy="170" r="258" fill="var(--sky)"/>
      <rect x="0" y="440" width="880" height="30" fill="var(--ink)"/>
      <rect x="0" y="470" width="880" height="40" fill="var(--sky)"/>
    </svg>
    <div class="back__logo">Farrugia's<br>Quality Meats</div>
    <div class="back__details">
      <p class="shop">Shop 9, Ridgeway Court,<br>Ashcombe NSW 2391<br><span class="label">Ph</span> 02 6512 3840</p>
      <p class="shop">47 Marlow St,<br>Kellbrook NSW 2394<br><span class="label">Ph</span> 02 6518 2274</p>
      <p class="abn">ABN 48 907 215 816</p>
    </div>
  </section>

</main>
</body>
</html>
```